Layout for site fence advertising - length approx. 250 cm x 125 cm

The advertising will later be printed on a PVC film and used for events or on sports fields.

Main services :
Your regional contact at
Real estate and business financing
independent insurance advice

```html
<!DOCTYPE html>
<html lang="en">
<head>
<meta charset="utf-8">
<title>Nordhain Finanzpartner – Site Fence Banner</title>
<link rel="stylesheet" href="https://fonts.googleapis.com/css2?family=Montserrat:wght@500;600;700;800&family=Quicksand:wght@500;600;700&display=swap">
<style>
  :root {
    --brand-blue: #1c4fb8;
    --ink-gray: #6f6f6f;
    --text-gray: #4a4a4a;
    --rule-gray: #9a9a9a;
    --paper: #ffffff;
    --stage: #e9eaec;
    --photo-light: #eeeeef;
    --photo-mid: #c9c3c1;
    --photo-dark: #2a2b36;
  }
  * { margin: 0; padding: 0; box-sizing: border-box; }
  html, body { width: 972px; height: 1200px; overflow: hidden; }
  body { background: var(--stage); position: relative; font-family: "Montserrat", sans-serif; }

  .banner {
    position: absolute; left: 26px; top: 370px;
    width: 920px; height: 460px;
    background: var(--paper);
    overflow: hidden;
    box-shadow: 0 6px 18px rgba(0,0,0,0.25);
  }

  .portrait {
    position: absolute; right: 0; top: 0;
    width: 330px; height: 460px;
    background:
      radial-gradient(ellipse 110px 140px at 56% 36%, var(--photo-mid) 0%, rgba(201,195,193,0) 100%),
      linear-gradient(180deg, var(--photo-light) 0%, var(--photo-light) 55%, var(--photo-dark) 78%, var(--photo-dark) 100%);
  }

  .brand-mark {
    position: absolute; left: 46px; top: 29px;
    width: 130px; height: 130px;
    border: 4px solid var(--brand-blue); border-radius: 50%;
  }
  .brand-divider {
    position: absolute; left: 188px; top: 31px;
    width: 3px; height: 130px; background: var(--text-gray);
  }
  .brand-name {
    position: absolute; left: 201px; top: 64px;
    font-family: "Quicksand", sans-serif; font-weight: 700;
    font-size: 26px; color: var(--brand-blue); white-space: nowrap;
  }
  .brand-tagline {
    position: absolute; left: 201px; top: 100px;
    font-family: "Quicksand", sans-serif; font-weight: 600;
    font-size: 18px; color: var(--text-gray); white-space: nowrap;
  }

  .headline-your {
    position: absolute; left: 46px; top: 174px;
    font-weight: 800; font-size: 43px; color: var(--ink-gray); line-height: 1;
  }
  .headline-rule {
    position: absolute; left: 163px; top: 205px;
    width: 370px; height: 1.5px; background: var(--rule-gray);
  }
  .headline-main {
    position: absolute; left: 44px; top: 220px;
    white-space: nowrap; line-height: 1;
  }
  .headline-regional { font-weight: 800; font-size: 62px; color: var(--brand-blue); }
  .headline-contact { font-weight: 800; font-size: 35px; color: var(--ink-gray); margin-left: 6px; }

  .section-rule {
    position: absolute; left: 43px; top: 301px;
    width: 501px; height: 1.5px; background: var(--rule-gray);
  }

  .service { position: absolute; top: 320px; display: flex; align-items: center; }
  .service--financing { left: 44px; }
  .service--insurance { left: 314px; }
  .service-icon { width: 36px; height: 36px; }
  .service-bar { width: 2px; height: 38px; background: var(--text-gray); margin: 0 8px 0 6px; }
  .service-label {
    font-weight: 600; font-size: 19px; line-height: 23px; color: var(--brand-blue); white-space: nowrap;
  }

  .contact-band {
    position: absolute; left: 0; top: 394px;
    width: 625px; height: 66px;
    background: var(--brand-blue);
    clip-path: polygon(0 0, 100% 0, 97.4% 100%, 0 100%);
    display: flex; align-items: center; padding-left: 42px; color: var(--paper);
  }
  .contact-icon { width: 20px; height: 20px; margin-right: 13px; }
  .contact-phone { font-weight: 800; font-size: 31px; letter-spacing: 0.3px; }
  .contact-bar { width: 2px; height: 30px; background: var(--paper); margin: 0 12px; }
  .contact-web { font-weight: 500; font-size: 25px; }
  .contact-web strong { font-weight: 700; }
</style>
</head>
<body>
  <section class="banner">
    <div class="portrait" role="img" aria-label="Portrait photo of the regional advisor in a dark suit and white shirt"></div>

    <div class="brand-mark" aria-hidden="true"></div>
    <div class="brand-divider"></div>
    <div class="brand-name">Nordhain Finanzpartner GmbH</div>
    <div class="brand-tagline">Finanzieren, Versichern, Vorsorgen</div>

    <div class="headline-your">Your</div>
    <div class="headline-rule"></div>
    <div class="headline-main">
      <span class="headline-regional">Regional</span><span class="headline-contact">Contact at</span>
    </div>
    <div class="section-rule"></div>

    <div class="service service--financing">
      <svg class="service-icon" viewBox="0 0 36 36" fill="none" stroke="#8a8a8a" stroke-width="1.6" stroke-linejoin="round">
        <path d="M4 17 L18 5 L32 17"/>
        <path d="M8 14 V30 H28 V14"/>
        <path d="M11 24 L16 20 L20 23 L25 19"/>
      </svg>
      <span class="service-bar"></span>
      <span class="service-label">Real estate and<br>Business financing</span>
    </div>

    <div class="service service--insurance">
      <svg class="service-icon" viewBox="0 0 36 36" fill="none" stroke="#8a8a8a" stroke-width="1.6" stroke-linejoin="round">
        <path d="M4 7 H32 V26 H14 L8 32 V26 H4 Z"/>
        <path d="M18 10 L24 12.5 V17 C24 20.5 21.5 22.5 18 24 C14.5 22.5 12 20.5 12 17 V12.5 Z"/>
      </svg>
      <span class="service-bar"></span>
      <span class="service-label">Independent<br>Insurance advice</span>
    </div>

    <div class="contact-band">
      <svg class="contact-icon" viewBox="0 0 20 20">
        <circle cx="10" cy="10" r="9" fill="none" stroke="#fff" stroke-width="2"/>
        <path d="M6.5 5.5 L8.5 5.5 L9.3 7.8 L8.2 8.8 C8.8 10 9.9 11.1 11.2 11.8 L12.2 10.7 L14.5 11.5 L14.5 13.5 C10 13.8 6.2 10 6.5 5.5 Z" fill="#fff"/>
      </svg>
      <span class="contact-phone">4567 456 789</span>
      <span class="contact-bar"></span>
      <svg class="contact-icon" viewBox="0 0 20 20" fill="none" stroke="#fff" stroke-width="1.5">
        <circle cx="10" cy="10" r="8.5"/>
        <ellipse cx="10" cy="10" rx="3.8" ry="8.5"/>
        <path d="M1.5 10 H18.5 M3 5.5 H17 M3 14.5 H17"/>
      </svg>
      <span class="contact-web">www.<strong>website</strong>.com</span>
    </div>
  </section>
</body>
</html>
```